Yacht Management in Miami & Ft Lauderdale (2019Q2)

I’m looking for a flyer to leave places for people to get information about my company and what services we offer.
We offer monthly management plans to ensure the vessel is ready to go at a moments notice. This can be as simple as washing once a week, or as involved as washing, waxing, detailing, provisioning, and crew services.
We also offer bespoke customizations; stereos, on board WiFi, and engineering.

Target Market(s)

Yacht and boat owners.

Font styles to use
Sans Serif

Colors
87d0c7
85cae6
85acd3
cedeed
cee9f5
cfeae6
0455a3

Requirements
Must have
• Must have simple attention grabbing, without being obnoxious.
• Prefer a 3in x 5in post card size. other size may be an option.
• Must be front and back.
Nice to have
• Languages: English, Spanish, Russian
• USA flag logo
Should not have
• Should not have a lot of text. Icons and photos are great.

```html
<!DOCTYPE html>
<html lang="en">
<head>
<meta charset="utf-8">
<title>Harbor Keepers – Postcard</title>
<link rel="stylesheet" href="https://fonts.googleapis.com/css2?family=Open+Sans:wght@300;400;600&display=swap">
<style>
  :root{
    --page:#ffffff;
    --ink:#111111;
    --front-panel:#c8d5ea;
    --front-stripe-a:#a6bfe0;
    --front-stripe-b:#85acd3;
    --back-panel:#cfe7e3;
    --back-stripe-a:#87d0c7;
    --back-stripe-b:#a6dcd5;
    --white:#ffffff;
    --label:#333333;
  }
  *{margin:0;padding:0;box-sizing:border-box}
  html,body{width:1200px;height:800px;overflow:hidden;background:var(--page)}
  body{position:relative;font-family:"Open Sans",sans-serif;color:var(--ink)}

  .card{position:absolute;top:208px;height:314px;width:523px;overflow:hidden}
  .card--front{left:67px}
  .card--back{left:617px}

  .panel{position:absolute;top:0;height:100%;text-align:center}
  .card--front .panel{left:0;width:165px;background:var(--front-panel)}
  .card--back .panel{left:358px;width:165px;background:var(--back-panel)}

  .stripe{position:absolute;top:0;height:100%}
  .stripe--front-a{left:165px;width:12px;background:var(--front-stripe-a)}
  .stripe--front-b{left:177px;width:8px;background:var(--front-stripe-b)}
  .stripe--back-a{left:338px;width:8px;background:var(--back-stripe-a)}
  .stripe--back-b{left:346px;width:12px;background:var(--back-stripe-b)}

  .photo{position:absolute;top:0;height:100%}
  .photo--hull{left:185px;width:338px;
    background:linear-gradient(160deg,#7f94a8 0%,#c7b9a8 22%,#f0c9a0 45%,#e9b48a 65%,#c9b9aa 82%,#9fb0bf 100%)}
  .photo--sunset{left:0;width:338px;
    background:linear-gradient(180deg,#3f4a57 0%,#7c7468 18%,#c99a5e 34%,#f0b765 46%,#e9a855 52%,#3a3630 60%,#57544f 75%,#8c8a86 88%,#6e6c6a 100%)}

  .headline{font-weight:300;line-height:25px;letter-spacing:-.2px}
  .card--front .headline{position:absolute;top:22px;left:0;width:100%;font-size:25px}
  .card--back .headline{position:absolute;top:20px;left:0;width:100%;font-size:21.5px;line-height:22px}

  .brand{position:absolute;left:0;width:100%;display:flex;flex-direction:column;align-items:center;gap:6px}
  .card--front .brand{top:160px}
  .card--back .brand{top:210px}
  .brand__dot{width:14px;height:14px;border-radius:50%;background:var(--ink)}
  .brand__name{font-size:15px;font-weight:600;line-height:17px;color:var(--ink)}

  .contact{position:absolute;top:104px;left:0;width:100%}
  .contact__web{font-size:16.5px;font-weight:300;line-height:22px}
  .contact__line{font-size:13px;font-weight:300;line-height:15px}
  .contact__web + .contact__line{margin-top:6px}

  .services{position:absolute;top:22px;left:18px;list-style:none}
  .service{display:flex;align-items:center;height:28px;color:var(--white);font-size:14px;font-weight:300;white-space:nowrap}
  .service svg{width:28px;height:22px;margin-right:10px;flex:none}

  .view-labels{position:absolute;top:741px;left:0;width:1200px;height:50px}
  .view-labels__divider{position:absolute;left:603px;top:0;width:1px;height:49px;background:var(--label)}
  .view-label{position:absolute;top:22px;font-size:11px;font-weight:300;color:var(--label)}
  .view-label--front{right:610px}
  .view-label--back{left:617px}
</style>
</head>
<body>

<section class="card card--front" aria-label="Postcard front">
  <div class="panel">
    <h1 class="headline">Complete<br>yacht service<br>you can trust</h1>
    <div class="brand">
      <span class="brand__dot"></span>
      <span class="brand__name">Harbor Keepers</span>
    </div>
  </div>
  <div class="stripe stripe--front-a"></div>
  <div class="stripe stripe--front-b"></div>
  <div class="photo photo--hull" role="img" aria-label="Photo of a white motor yacht's side rail cutting through the sea at sunset"></div>
</section>

<section class="card card--back" aria-label="Postcard back">
  <div class="photo photo--sunset" role="img" aria-label="Photo of a yacht's bow facing the sun setting over the ocean"></div>
  <ul class="services">
    <li class="service">
      <svg viewBox="0 0 28 22" fill="none" stroke="#fff" stroke-width="1.6" stroke-linecap="round"><circle cx="14" cy="3" r="1.8"/><path d="M14 5v15M10 8h8M6 14c1 4 5 6 8 6s7-2 8-6M6 14l-1.5 1.5M22 14l1.5 1.5"/></svg>
      Yacht service &amp; monthly management plans
    </li>
    <li class="service">
      <svg viewBox="0 0 28 22" fill="#fff"><rect x="11" y="1" width="6" height="4"/><rect x="8" y="5" width="12" height="5" rx="1"/><path d="M5 11h18l-3 9H8z"/></svg>
      Bespoke refits, updates &amp; customizations
    </li>
    <li class="service">
      <svg viewBox="0 0 28 22" fill="none" stroke="#fff" stroke-width="1.6"><rect x="9" y="1" width="10" height="20" rx="1.5" fill="#fff"/><circle cx="14" cy="7" r="1.8" fill="#333" stroke="none"/><circle cx="14" cy="14.5" r="3" fill="#333" stroke="none"/><path d="M6 7c-2 2-2 6 0 8M3 5c-3 3-3 9 0 12M22 7c2 2 2 6 0 8M25 5c3 3 3 9 0 12"/></svg>
      Stereo packages &amp; on-board wi-fi
    </li>
    <li class="service">
      <svg viewBox="0 0 28 22" fill="none" stroke="#fff" stroke-width="1.6"><ellipse cx="14" cy="11" rx="12.5" ry="8"/><path d="M5 13c3-2 15-2 18 0" /><circle cx="14" cy="8" r="2" fill="#fff"/></svg>
      Captaining and crew services
    </li>
    <li class="service">
      <svg viewBox="0 0 28 22" fill="none" stroke="#fff" stroke-width="1.6"><rect x="2" y="1" width="24" height="16"/><path d="M9 21h10M14 17v4M10 9l3 3 5-6"/></svg>
      Internet sales for DIY installations
    </li>
  </ul>
  <div class="stripe stripe--back-a"></div>
  <div class="stripe stripe--back-b"></div>
  <div class="panel">
    <h2 class="headline">Contact us to<br>find out more</h2>
    <address class="contact" style="font-style:normal">
      <p class="contact__web">harborkeepers.us</p>
      <p class="contact__line">call: (954) 555-0182</p>
      <p class="contact__line">email: info@harborkeepers.us</p>
    </address>
    <div class="brand">
      <span class="brand__dot"></span>
      <span class="brand__name">Harbor Keepers</span>
    </div>
  </div>
</section>

<div class="view-labels">
  <span class="view-label view-label--front">FRONT</span>
  <span class="view-labels__divider"></span>
  <span class="view-label view-label--back">BACK</span>
</div>

</body>
</html>
```